Our Family Values Printed on Canvas for our Home

My family has decided on the following values:

Be Grateful
Act Kindly
Stay Honest
Smile Often
Do Your Best
Live Adventurously
Never Stop Learning
Help Others
Love Always

We desire to print a sign (on 16x20 or 20x16 canvas) for various rooms in our house to remind us of the family we want to be. Each value has equal value, and we want the sign to reflect that (for example, we don't want one value to appear larger than another). We are not particular about colors or images however here are some hints about us that may help:
- My wife's favorite color is dark teal
- We live in the Pacific Northwest
- We love nature
- My wife and I have two sons and a dog

We look forward to your design!

--Tobias

Target Market(s)

Our family and friends

Industry/Entity Type

Non-Profit

Font styles to use
Decorative

Requirements
Must have
• - Printable on 16x20 or 20x60 canvas
• - Equal emphasis on each value
• - Easy to read

```html
<!DOCTYPE html>
<html lang="en">
<head>
<meta charset="utf-8">
<title>Family Values Canvas Set</title>
<link rel="stylesheet" href="https://fonts.googleapis.com/css2?family=Quicksand:wght@400;700&display=swap">
<style>
  :root {
    --backdrop: #85867f;
    --frame: #e4e4e2;
    --frame-edge: #c9c9c6;
    --ink: #ffffff;
    --grateful: #14906f;
    --kindly: #0f5a8f;
    --honest: #7a8a26;
    --smile: #9a1a5c;
    --adventure: #117087;
    --best: #8c7620;
    --learning: #199446;
    --help: #5a2596;
    --love: #2838a0;
    --shade: #05070a;
  }
  * { box-sizing: border-box; margin: 0; padding: 0; }
  html, body {
    width: 1200px;
    height: 761px;
    overflow: hidden;
  }
  body {
    background: var(--backdrop);
    font-family: "Quicksand", sans-serif;
  }
  .value-wall {
    position: relative;
    width: 1200px;
    height: 761px;
  }
  .print {
    position: absolute;
    border: 7px solid var(--frame);
    box-shadow: 0 0 0 1px var(--frame-edge), 2px 4px 10px rgba(0,0,0,0.25);
    overflow: hidden;
  }
  .print--wide { width: 236px; height: 188px; }
  .print--tall { width: 188px; height: 236px; }
  .print__art {
    position: absolute;
    inset: 0;
    background:
      radial-gradient(ellipse at 55% 60%, var(--tone) 0%, color-mix(in srgb, var(--tone) 70%, var(--shade)) 55%, var(--shade) 120%);
  }
  .print__words {
    position: absolute;
    inset: 0;
    display: flex;
    flex-direction: column;
    align-items: center;
    justify-content: center;
    color: var(--ink);
    font-size: 31px;
    line-height: 39px;
    text-align: center;
    letter-spacing: -0.3px;
    text-shadow: 0 1px 3px rgba(0,0,0,0.45);
    white-space: nowrap;
  }
  .print__lead { font-weight: 400; }
  .print__key { font-weight: 700; }

  .print--grateful   { left: 256px; top: 59px;  --tone: var(--grateful); }
  .print--kindly     { left: 507px; top: 35px;  --tone: var(--kindly); }
  .print--honest     { left: 710px; top: 59px;  --tone: var(--honest); }
  .print--smile      { left: 280px; top: 264px; --tone: var(--smile); }
  .print--adventure  { left: 483px; top: 287px; --tone: var(--adventure); }
  .print--best       { left: 734px; top: 264px; --tone: var(--best); }
  .print--learning   { left: 256px; top: 515px; --tone: var(--learning); }
  .print--help       { left: 507px; top: 491px; --tone: var(--help); }
  .print--love       { left: 710px; top: 515px; --tone: var(--love); }
  .print--adventure .print__words { font-size: 30px; letter-spacing: -0.8px; }
</style>
</head>
<body>
<main class="value-wall">
  <article class="print print--wide print--grateful">
    <div class="print__art" role="img" aria-label="Dark teal-green feathery palm fronds"></div>
    <div class="print__words"><span class="print__lead">Be</span><span class="print__key">Grateful</span></div>
  </article>
  <article class="print print--tall print--kindly">
    <div class="print__art" role="img" aria-label="Deep blue feathery palm fronds"></div>
    <div class="print__words"><span class="print__lead">Act</span><span class="print__key">Kindly</span></div>
  </article>
  <article class="print print--wide print--honest">
    <div class="print__art" role="img" aria-label="Olive green feathery palm fronds"></div>
    <div class="print__words"><span class="print__lead">Stay</span><span class="print__key">Honest</span></div>
  </article>
  <article class="print print--tall print--smile">
    <div class="print__art" role="img" aria-label="Magenta feathery palm fronds"></div>
    <div class="print__words"><span class="print__lead">Smile</span><span class="print__key">Often</span></div>
  </article>
  <article class="print print--wide print--adventure">
    <div class="print__art" role="img" aria-label="Dark teal feathery palm fronds"></div>
    <div class="print__words"><span class="print__lead">Live</span><span class="print__key">Adventurously</span></div>
  </article>
  <article class="print print--tall print--best">
    <div class="print__art" role="img" aria-label="Ochre gold feathery palm fronds"></div>
    <div class="print__words"><span class="print__lead">Do</span><span class="print__key">Your Best</span></div>
  </article>
  <article class="print print--wide print--learning">
    <div class="print__art" role="img" aria-label="Bright green feathery palm fronds"></div>
    <div class="print__words"><span class="print__lead">Never</span><span class="print__lead">Stop</span><span class="print__lead">Learning</span></div>
  </article>
  <article class="print print--tall print--help">
    <div class="print__art" role="img" aria-label="Violet feathery palm fronds"></div>
    <div class="print__words"><span class="print__lead">Help</span><span class="print__key">Others</span></div>
  </article>
  <article class="print print--wide print--love">
    <div class="print__art" role="img" aria-label="Royal blue feathery palm fronds"></div>
    <div class="print__words"><span class="print__lead">Love</span><span class="print__key">Always</span></div>
  </article>
</main>
</body>
</html>
```